Flint Yard Strategy Powerpoint Template

We require a powerpoint template, including an appropriate colour palette, for our marketing consultancy called "Flint Yard Strategy". We specialise in B2B Marketing & Innovation strategy for the life sciences and digital healthcare industries.
Our logo has already been designed and we have adopted two font styles for our communications so far: Bebas Neue and Bitter.
Our brand is heavily based around a contemporary industrial style and incorporates elements from east Londons design scene. In fact, our logo and brand was inspired by the street signs around flint yard in east London. Currently we use a template that uses various grey, black and off-white tones to reflect a industrial style and would like to keep clean creative innovative style. However, we are open to seeing additional colour proposals, as long as they retain the modern industrial feel.

Industry/Entity Type

Business Consultant

Colors

Designer to choose colors to be used in the design.

Requirements
Must have
• Our logo has already been designed and we have adopted two font styles for our communications so far: Bebas Neue and Bitter.
• Our brand is heavily based around a contemporary industrial style and incorporates elements from east Londons design scene. In fact, our logo and brand was inspired by the street signs around flint yard in east London.
• creative shapes and images to drop in
Nice to have
• owever, we are open to seeing additional colour proposals, as long as they retain the modern industrial feel
Should not have
• too corporate,

```html
<!DOCTYPE html>
<html lang="en">
<head>
<meta charset="utf-8">
<title>Flint Yard Strategy – Presentation Template</title>
<link rel="stylesheet" href="https://fonts.googleapis.com/css2?family=Arimo:wght@400;700&display=swap">
<style>
  :root {
    --ink: #000000;
    --blue: #13a6e6;
    --sky: #1ab0ec;
    --white: #ffffff;
    --rule: #3a3f44;
    --rule-light: #9fd6f0;
    --body-dark: #e8e8e8;
    --body-light: #444444;
  }
  * { box-sizing: border-box; margin: 0; padding: 0; }
  html, body { width: 1040px; height: 1200px; overflow: hidden; background: var(--white); }
  body { position: relative; font-family: "Arimo", Arial, sans-serif; }

  .slide { position: absolute; width: 492px; height: 277px; overflow: hidden; background: var(--ink); }
  .col-a { left: 18px; } .col-b { left: 529px; }
  .row-1 { top: 18px; } .row-2 { top: 314px; } .row-3 { top: 609px; } .row-4 { top: 904px; }
  .slide--light { background: var(--white); }

  .photo { position: absolute; inset: 0; }
  .photo--dusk { background: linear-gradient(170deg, #1b1d20 0%, #0d0e10 55%, #050505 100%); }
  .photo--sky { background: linear-gradient(175deg, #21b3ee 0%, #14a7e6 60%, #0f9fdd 100%); }
  .photo--tower { background: linear-gradient(160deg, #3a3d42 0%, #8b8f95 35%, #2a2c30 65%, #0e0f11 100%); }
  .photo--clouds { background: radial-gradient(ellipse at 70% 20%, #d9dadc 0%, #8a8c90 35%, #3a3c40 70%, #141517 100%); }

  .brand { position: absolute; display: flex; align-items: center; gap: 5px; color: var(--white); font-weight: 400; white-space: nowrap; }
  .brand::before { content: ""; display: block; width: .8em; height: .8em; background: var(--blue); }
  .brand--lg { font-size: 11px; }
  .brand--xl { font-size: 15px; }
  .brand--sm { font-size: 6px; gap: 3px; right: 20px; top: 28px; }
  .slide--light .brand--sm { color: var(--ink); }

  .title-band { position: absolute; right: 0; height: 54px; background: var(--ink); padding: 3px 0 0 28px; }
  .title-band::before { content: ""; position: absolute; left: 0; top: 0; width: 4px; height: 100%; background: var(--blue); }
  .title-band--blackedge::before { background: var(--ink); box-shadow: 3px 0 0 var(--sky); }
  .title-band h1 { font-weight: 400; font-size: 21px; color: var(--blue); line-height: 28px; }
  .title-band p { font-size: 14px; color: var(--white); line-height: 17px; }

  .heading { position: absolute; left: 18px; top: 8px; height: 37px; padding-left: 11px; border-left: 1px solid #8a8a8a; }
  .heading::before, .heading::after { content: ""; position: absolute; left: -1px; width: 4px; border-top: 1px solid #8a8a8a; }
  .heading::before { top: 0; } .heading::after { bottom: 0; }
  .heading h2 { font-weight: 400; font-size: 22px; color: var(--blue); line-height: 37px; }

  .column { position: absolute; top: 70px; width: 206px; }
  .column--left { left: 18px; } .column--right { left: 251px; }
  .column h3 { font-size: 6.8px; font-weight: 700; color: var(--blue); margin-bottom: 7px; }
  .column p, .column li { font-size: 6.6px; line-height: 10.6px; color: var(--body-dark); }
  .slide--light .column p { color: var(--body-light); }
  .column ul { list-style: none; }
  .column li { position: relative; padding-left: 13px; line-height: 8.4px; margin-bottom: 5px; }
  .column li::before { content: "•"; position: absolute; left: 0; }
  .column li.sub { padding-left: 26px; }
  .column li.sub::before { left: 13px; }

  .footer-rule { position: absolute; left: 9px; width: 470px; top: 258px; border-top: 1px solid var(--rule); }
  .footer-rule::after { content: ""; position: absolute; right: -5px; top: -3.5px; width: 6px; height: 6px; border-radius: 50%; background: var(--white); }
  .slide--light .footer-rule { border-color: var(--rule-light); }
  .slide--light .footer-rule::after { background: var(--blue); }

  .process-band { position: absolute; left: 0; top: 176px; width: 100%; height: 69px; background: var(--sky); }

  .map { position: absolute; left: 60px; top: 60px; width: 370px; height: 170px; background: radial-gradient(ellipse, #101214 0%, rgba(0,0,0,0) 70%); }
  .stat { position: absolute; top: 66px; width: 118px; }
  .stat svg { display: block; margin-left: 12px; }
  .stat p { font-size: 6.4px; line-height: 10.6px; color: var(--body-dark); margin-top: 3px; }

  .thanks-band { position: absolute; left: 119px; right: 0; top: 145px; height: 54px; background: var(--ink); text-align: center; }
  .thanks-band h1 { font-weight: 400; font-size: 36px; line-height: 54px; color: var(--blue); }
  .address-band { position: absolute; left: 0; right: 0; top: 228px; height: 23px; background: var(--sky); text-align: center; font-size: 14px; line-height: 23px; color: var(--white); }
</style>
</head>
<body>

<section class="slide col-a row-1">
  <div class="photo photo--dusk" role="img" aria-label="Dark upward view of glass office towers"></div>
  <div class="brand brand--lg" style="left:366px;top:42px">Flint Yard Strategy</div>
  <div class="title-band" style="left:28px;top:145px"><h1>Presentation Title</h1><p>Subtitle</p></div>
</section>

<section class="slide col-b row-1">
  <div class="photo photo--sky" role="img" aria-label="Blue-tinted upward view of glass office towers"></div>
  <div class="brand brand--lg" style="left:366px;top:42px">Flint Yard Strategy</div>
  <div class="title-band title-band--blackedge" style="left:28px;top:145px"><h1>Presentation Title</h1><p>Subtitle</p></div>
</section>

<section class="slide col-a row-2">
  <div class="heading"><h2>Presentation Title</h2></div>
  <div class="brand brand--sm">Flint Yard Strategy</div>
  <div class="column column--left"><h3>Sub-Heading 1</h3>
    <p>It is a long established fact that a reader will be distracted by the readable content of a page when looking at its layout. The point of using Lorem Ipsum is that it has a more-or-less normal distribution of letters, as opposed to using 'Content here, content here', making it look li model text, and a search for 'lorem ipsum' will uncover many web sites still in their infancy. Various versions have evolved over the years, sometimes by accident, sometimes on purpose (injected humour and the like).</p></div>
  <div class="column column--right"><h3>Sub-Heading 2</h3>
    <p>It is a long established fact that a reader will be distracted by the readable content of a page when looking at its layout. The point of using Lorem Ipsum is that it has a more-or-less normal distribution of letters, as opposed to using 'Content here, content here', making it look li model text, and a search for 'lorem ipsum' will uncover many web sites still in their infancy. Various versions have evolved over the years, sometimes by accident, sometimes on purpose (injected humour and the like).</p></div>
  <div class="footer-rule"></div>
</section>

<section class="slide slide--light col-b row-2">
  <div class="heading"><h2>Presentation Title</h2></div>
  <div class="brand brand--sm">Flint Yard Strategy</div>
  <div class="column column--left"><h3>Sub-Heading 1</h3>
    <p>It is a long established fact that a reader will be distracted by the readable content of a page when looking at its layout. The point of using Lorem Ipsum is that it has a more-or-less normal distribution of letters, as opposed to using 'Content here, content here', making it look li model text, and a search for 'lorem ipsum' will uncover many web sites still in their infancy. Various versions have evolved over the years, sometimes by accident, sometimes on purpose (injected humour and the like).</p></div>
  <div class="column column--right"><h3>Sub-Heading 2</h3>
    <p>It is a long established fact that a reader will be distracted by the readable content of a page when looking at its layout. The point of using Lorem Ipsum is that it has a more-or-less normal distribution of letters, as opposed to using 'Content here, content here', making it look li model text, and a search for 'lorem ipsum' will uncover many web sites still in their infancy. Various versions have evolved over the years, sometimes by accident, sometimes on purpose (injected humour and the like).</p></div>
  <div class="footer-rule"></div>
</section>

<section class="slide col-a row-3">
  <div class="heading"><h2>Presentation Title</h2></div>
  <div class="brand brand--sm">Flint Yard Strategy</div>
  <div class="column column--left"><h3>Sub-Heading 1</h3>
    <ul>
      <li>It is a long established fact that a reader will be distracted by the readable content of a page</li>
      <li>When looking at its layout. The point of using Lorem Ipsum is that it has a more-or-less normal distribution of letters</li>
      <li>As opposed to using 'Content here, content here', making it look like readable English.</li>
      <li>Many desktop publishing packages and web page editors now use Lorem Ipsum as their default model text.humour and the like).</li>
    </ul></div>
  <div class="column column--right"><h3>Sub-Heading 2</h3>
    <ul>
      <li>It is a long established fact that a reader will be distracted by the readable content of a page</li>
      <li class="sub">When looking at its layout. The point of using Lorem Ipsum is that it has a more-or-less normal distribution of letters</li>
      <li class="sub">As opposed to using 'Content here, content here', making it look like readable English.</li>
      <li class="sub">Many desktop publishing packages and web page editors now use Lorem Ipsum as their default model text.humour and the like).</li>
    </ul></div>
  <div class="process-band">
    <svg width="492" height="69" viewBox="0 0 492 69" aria-label="Process steps: idea, iterate, launch, operate">
      <g fill="#000">
        <circle cx="142" cy="34.5" r="24"/><circle cx="211" cy="34.5" r="24"/>
        <circle cx="280" cy="34.5" r="24"/><circle cx="349" cy="34.5" r="24"/>
        <path d="M171 28 l7 6.5 l-7 6.5z M240 28 l7 6.5 l-7 6.5z M309 28 l7 6.5 l-7 6.5z"/>
      </g>
      <g fill="none" stroke="#fff" stroke-width="2" stroke-linecap="round">
        <path d="M136 41 v-3 c-4 -3 -5 -6 -5 -9 a11 11 0 0 1 22 0 c0 3 -1 6 -5 9 v3z"/>
        <path d="M137 44 h10 M138 47 h8"/>
        <path d="M201 30 a11 11 0 0 1 19 -3"/><path d="M221 39 a11 11 0 0 1 -19 3"/>
        <path d="M220 21 v6 h-6 M202 48 v-6 h6"/>
        <path d="M273 27 a10 10 0 1 0 14 0"/><path d="M280 22 v11"/>
      </g>
      <g fill="#fff">
        <circle cx="345" cy="38" r="7"/><circle cx="355" cy="28" r="5"/>
        <circle cx="345" cy="38" r="2.5" fill="#000"/><circle cx="355" cy="28" r="1.8" fill="#000"/>
        <path d="M343 28 h4 v3 h-4z M343 45 h4 v3 h-4z M335 36 h3 v4 h-3z M352 36 h3 v4 h-3z M353 20 h4 v3 h-4z M361 26 h3 v4 h-3z"/>
      </g>
    </svg>
  </div>
  <div class="footer-rule"></div>
</section>

<section class="slide col-b row-3">
  <div class="photo photo--tower" role="img" aria-label="Black and white upward view of glass skyscrapers under a cloudy sky"></div>
  <div class="brand brand--lg" style="left:36px;top:44px">Flint Yard Strategy</div>
  <div class="title-band" style="left:216px;top:143px"><h1>Presentation Title</h1><p>Subtitle</p></div>
</section>

<section class="slide col-a row-4">
  <div class="heading"><h2>Presentation Title</h2></div>
  <div class="brand brand--sm">Flint Yard Strategy</div>
  <div class="map" role="img" aria-label="Faint world map in the background"></div>
  <div class="stat" style="left:61px">
    <svg width="64" height="64" viewBox="0 0 64 64"><path d="M36 3 A29 29 0 0 1 36 61" fill="none" stroke="#fff" stroke-width="2.5"/><path d="M24 5 A29 29 0 0 0 10 48" fill="none" stroke="#fff" stroke-width="2.5"/><text x="32" y="37" text-anchor="middle" fill="#fff" font-size="14" font-family="Arimo, sans-serif">30%</text></svg>
    <p>It is a long established fact that a reader will be distracted by the readable content of a page. The point of using Lorem Ipsum is that it has a more-or-less distribution of letters, as opposed to using 'Content here, content here.</p></div>
  <div class="stat" style="left:188px">
    <svg width="64" height="64" viewBox="0 0 64 64"><path d="M34 3 A29 29 0 0 1 58 44" fill="none" stroke="#fff" stroke-width="2.5"/><path d="M22 5 A29 29 0 0 0 40 60" fill="none" stroke="#fff" stroke-width="2.5"/><text x="32" y="37" text-anchor="middle" fill="#fff" font-size="14" font-family="Arimo, sans-serif">30%</text></svg>
    <p>It is a long established fact that a reader will be distracted by the readable content of a page. The point of using Lorem Ipsum is that it has a more-or-less distribution of letters, as opposed to using 'Content here, content here.</p></div>
  <div class="stat" style="left:315px">
    <svg width="64" height="64" viewBox="0 0 64 64"><path d="M38 4 A29 29 0 0 1 50 55" fill="none" stroke="#fff" stroke-width="2.5"/><path d="M12 53 A29 29 0 0 0 44 59" fill="none" stroke="#fff" stroke-width="2.5"/><text x="32" y="37" text-anchor="middle" fill="#fff" font-size="14" font-family="Arimo, sans-serif">30%</text></svg>
    <p>It is a long established fact that a reader will be distracted by the readable content of a page. The point of using Lorem Ipsum is that it has a more-or-less distribution of letters, as opposed to using 'Content here, content here.</p></div>
  <div class="footer-rule"></div>
</section>

<section class="slide col-b row-4">
  <div class="photo photo--clouds" role="img" aria-label="Black and white skyscrapers beneath dramatic clouds"></div>
  <div class="brand brand--xl" style="left:176px;top:52px">Flint Yard Strategy</div>
  <div class="thanks-band"><h1>Thank You</h1></div>
  <div class="address-band">Street | City | State | Zip codes</div>
</section>

</body>
</html>
```